Corporate flyer introducing a brand new technology apprenticeship program in Australia!

A professional, yet clean and contemporary looking flyer to advertise a brand new service offering in a simple, easy to read format with engaging images. Here is a link to our current online brochure which outlines the program we would like to advertise in a hardcopy flyer/brochure format: https://pages.vendrap.com/Information-on-Technology-Higher-Apprenticeships-for-Employers-Victoria-kT3pzqW7LmRe

Target Market(s)

Medium to large sized businesses involved in using cutting edge technology, such as engineering and advanced manufracturing (3D printing etc)

Industry/Entity Type

Engineering

Colors

Designer to choose colors to be used in the design.

Requirements
Must have
• Contemporary, clean looking, easy to read, tech/engineering/advanced manufacturing related imagery
Nice to have
• Some ideas about different sizes/styles (eg something other than a plain A4 sheet)
Should not have
• Unprofessional or offensive language

```html
<!DOCTYPE html>
<html lang="en">
<head>
<meta charset="utf-8">
<title>Technology Higher Apprentices – Brochure Covers</title>
<link rel="stylesheet" href="https://fonts.googleapis.com/css2?family=Montserrat:wght@400;600;800&family=Lato:wght@400&display=swap">
<style>
  :root {
    --crimson: #8a2a40;
    --crimson-light: #9b3049;
    --slate: #3b4352;
    --slate-light: #566178;
    --slate-dark: #2e3440;
    --paper: #ffffff;
    --backdrop: #c9c9cb;
    --photo-warm: #a88c62;
    --photo-green: #4f6b3a;
  }
  * { margin: 0; padding: 0; box-sizing: border-box; }
  html, body { width: 1200px; height: 789px; overflow: hidden; background: var(--backdrop); }
  .spread {
    position: absolute; left: 105px; top: 45px;
    width: 990px; height: 700px;
    display: flex;
    box-shadow: 0 10px 30px rgba(0,0,0,.18);
  }
  .page { position: relative; width: 495px; height: 700px; overflow: hidden; }

  /* Back cover */
  .back-cover { background: var(--crimson); }
  .back-cover__rule {
    position: absolute; left: 0; right: 60px; top: 70px;
    height: 2px; background: rgba(255,255,255,.85);
  }
  .back-cover__brand {
    position: absolute; top: 230px; left: 0; right: 0;
    display: flex; justify-content: center; align-items: center; gap: 10px;
  }
  .back-cover__brand-mark { width: 14px; height: 14px; background: var(--paper); }
  .back-cover__brand-name {
    font-family: 'Montserrat', sans-serif; font-weight: 800;
    font-size: 40px; letter-spacing: 2px; color: var(--paper);
  }
  .back-cover__band {
    position: absolute; left: 0; right: 0; top: 400px; height: 270px;
    background: radial-gradient(ellipse at 60% 40%, var(--slate-light), var(--slate) 55%, var(--slate-dark));
    display: flex; flex-direction: column; align-items: center; justify-content: center; gap: 22px;
  }
  .contact-item {
    display: flex; flex-direction: column; align-items: center; gap: 6px;
    font-family: 'Lato', sans-serif; font-size: 13px; letter-spacing: .5px; color: #e9ebef;
  }
  .contact-item svg { width: 14px; height: 14px; }
  .back-cover__strip { position: absolute; left: 0; right: 0; bottom: 0; height: 30px; background: var(--crimson); }

  /* Front cover */
  .front-cover { background: var(--paper); border-left: 1px solid rgba(0,0,0,.08); }
  .front-cover__header {
    height: 98px; display: flex; align-items: center; justify-content: center; gap: 16px;
  }
  .front-cover__brand {
    font-family: 'Montserrat', sans-serif; font-weight: 800;
    font-size: 22px; color: var(--crimson); letter-spacing: 1px;
  }
  .front-cover__divider { width: 1px; height: 48px; background: #9aa0aa; }
  .front-cover__unit { font-family: 'Montserrat', sans-serif; line-height: 1; }
  .front-cover__unit-title { font-weight: 400; font-size: 21px; color: var(--slate-dark); letter-spacing: .5px; }
  .front-cover__unit-sub { font-weight: 600; font-size: 9px; color: var(--crimson); letter-spacing: .5px; margin-top: 5px; }
  .front-cover__photo {
    height: 262px;
    background: linear-gradient(120deg, var(--photo-warm) 0%, #d8cfc0 35%, #6e5a3e 60%, var(--photo-green) 100%);
  }
  .front-cover__band {
    position: absolute; left: 0; right: 0; top: 360px; height: 310px;
    background: radial-gradient(ellipse at 35% 35%, var(--slate-light), var(--slate) 55%, var(--slate-dark));
    display: flex; align-items: center; justify-content: center;
  }
  .front-cover__title {
    font-family: 'Montserrat', sans-serif; font-weight: 800;
    font-size: 44px; line-height: 1.12; color: var(--paper); text-align: center;
  }
  .front-cover__strip { position: absolute; left: 0; right: 0; bottom: 0; height: 30px; background: var(--crimson-light); }
</style>
</head>
<body>
<main class="spread">
  <section class="page back-cover">
    <div class="back-cover__rule"></div>
    <div class="back-cover__brand">
      <span class="back-cover__brand-mark"></span>
      <span class="back-cover__brand-name">VANTRA</span>
    </div>
    <div class="back-cover__band">
      <div class="contact-item">
        <svg viewBox="0 0 16 16" fill="none" stroke="#e9ebef" stroke-width="1.3"><rect x="1.5" y="3.5" width="13" height="9"/><path d="M1.5 3.5 8 9l6.5-5.5"/></svg>
        <span>talent@vantragroup.com.au</span>
      </div>
      <div class="contact-item">
        <svg viewBox="0 0 16 16" fill="none" stroke="#e9ebef" stroke-width="1.3"><path d="M4 2h3l1 3.5-2 1.2a8 8 0 0 0 3.3 3.3l1.2-2L14 9v3a2 2 0 0 1-2 2A10 10 0 0 1 2 4a2 2 0 0 1 2-2z"/></svg>
        <span>1300 555 014</span>
      </div>
      <div class="contact-item">
        <svg viewBox="0 0 16 16" fill="none" stroke="#e9ebef" stroke-width="1.2"><circle cx="8" cy="8" r="6.5"/><ellipse cx="8" cy="8" rx="3" ry="6.5"/><path d="M1.5 8h13M2.5 5h11M2.5 11h11"/></svg>
        <span>www.vantragroup.com.au</span>
      </div>
    </div>
    <div class="back-cover__strip"></div>
  </section>

  <section class="page front-cover">
    <header class="front-cover__header">
      <span class="front-cover__brand">VANTRA</span>
      <span class="front-cover__divider"></span>
      <div class="front-cover__unit">
        <div class="front-cover__unit-title">TALENT<br>SOLUTIONS</div>
        <div class="front-cover__unit-sub">WORKFORCE DEVELOPMENT</div>
      </div>
    </header>
    <div class="front-cover__photo" role="img" aria-label="Photo of two professionals meeting at an outdoor table with a laptop and tablet, greenery in the foreground"></div>
    <div class="front-cover__band">
      <h1 class="front-cover__title">Technology<br>Higher<br>Apprentices</h1>
    </div>
    <div class="front-cover__strip"></div>
  </section>
</main>
</body>
</html>
```